Silver Kettle Consulting

I need a business card design and for my consulting business. I provide outsourced CFO services for start-ups and high growth companies. I call my company Silver Kettle because building a company is similar to building a stone pathway, selecting each stone and planning several stones head in order to properly place them - all while keeping an eye on the final design and curve of the path. The underlying idea I want to express with my marketing images is that I'm someone that you can count on to help build your business and be there step by step to help. I'm not the old gray-haired CFO that many folks think of. :) I've included a one-page summery that I'm working on, it includes a summary of what I do. I've used a muted pathway and with greens in the header , and do like the green, but am open to other colors if they work well. Would like something that looks like a pathway, but a more abstract version instead of a picture.

Marketing

```html
<!DOCTYPE html>
<html lang="en">
<head>
<meta charset="utf-8">
<title>Silver Kettle Consulting – Business Card</title>
<link rel="stylesheet" href="https://fonts.googleapis.com/css2?family=Cormorant+SC:wght@500;600&family=Cormorant+Garamond:wght@500;600&family=Open+Sans:wght@400;600&display=swap">
<style>
  :root {
    --page: #e9e6df;
    --card-white: #fbfbfa;
    --ink: #2f2f2f;
    --ink-soft: #555;
    --band-dark: #141414;
    --band-mid: #2a2a2a;
    --green: #14915a;
    --green-deep: #0b6e3f;
    --green-light: #2aa66c;
    --on-green: #f4f8f5;
  }
  * { box-sizing: border-box; margin: 0; padding: 0; }
  html, body { width: 1200px; height: 1023px; overflow: hidden; }
  body { background: var(--page); position: relative; font-family: "Open Sans", Arial, sans-serif; }

  .card {
    position: absolute;
    width: 600px;
    height: 343px;
    border-radius: 4px;
    overflow: hidden;
    box-shadow: 0 10px 28px rgba(0,0,0,.18);
  }

  /* ---------- Front ---------- */
  .card--front { left: 90px; top: 80px; background: var(--card-white); }
  .front-top { position: absolute; inset: 0 0 132px 0; }
  .brand {
    position: absolute; left: 36px; top: 70px;
    display: flex; align-items: center; gap: 10px;
    font-family: "Cormorant Garamond", Georgia, serif;
    font-weight: 600; font-size: 34px; color: var(--green);
    line-height: 1;
  }
  .brand-dot { width: 14px; height: 14px; border-radius: 50%; background: var(--green); }
  .front-heading {
    position: absolute; right: 40px; top: 38px; width: 300px; text-align: center;
  }
  .tagline {
    font-family: "Cormorant SC", Georgia, serif; font-weight: 500;
    font-size: 23px; line-height: 1.2; color: var(--ink); letter-spacing: .5px;
  }
  .rule { height: 1px; background: var(--green); margin: 12px 20px 10px; }
  .person-name {
    font-family: "Cormorant SC", Georgia, serif; font-weight: 600;
    font-size: 22px; color: var(--green); letter-spacing: .5px;
  }
  .person-title {
    font-family: "Cormorant SC", Georgia, serif; font-weight: 500;
    font-size: 14px; color: var(--ink-soft); letter-spacing: 1px;
  }
  .rule--bottom { margin: 10px 20px 0; }

  .front-band {
    position: absolute; left: 0; right: 0; bottom: 10px; height: 122px;
    background: linear-gradient(180deg, var(--band-mid), var(--band-dark));
    color: #f2f2f2; padding: 22px 36px;
    display: flex; justify-content: space-between;
  }
  .front-stripe { position: absolute; left: 0; right: 0; bottom: 0; height: 10px; background: var(--green); }
  .contact-list { list-style: none; font-size: 15px; line-height: 26px; }
  .contact-list li { display: flex; align-items: center; gap: 10px; }
  .contact-icon { width: 14px; height: 14px; border-radius: 2px; background: var(--green); display: inline-flex; align-items: center; justify-content: center; }
  .address { font-size: 15px; line-height: 26px; text-align: left; }
  .address .company { color: var(--green-light); font-weight: 600; }

  /* ---------- Back ---------- */
  .card--back {
    left: 510px; top: 580px;
    background: linear-gradient(160deg, var(--green-light) 0%, var(--green) 45%, var(--green-deep) 100%);
    color: var(--on-green);
  }
  .back-brand {
    position: absolute; right: 60px; top: 62px;
    display: flex; align-items: center; gap: 12px;
    font-family: "Cormorant Garamond", Georgia, serif;
    font-weight: 600; font-size: 40px; color: var(--on-green); line-height: 1;
  }
  .back-brand .brand-dot { background: var(--on-green); width: 16px; height: 16px; }
  .back-rule { position: absolute; left: 0; right: 0; top: 170px; height: 1px; background: rgba(255,255,255,.7); }
  .back-question {
    position: absolute; left: 40px; top: 184px;
    font-family: "Cormorant SC", Georgia, serif; font-weight: 500;
    font-size: 21px; letter-spacing: .8px;
  }
  .services { position: absolute; left: 40px; top: 226px; list-style: none; font-size: 14px; line-height: 24px; }
</style>
</head>
<body>

<section class="card card--front" aria-label="Business card front">
  <div class="front-top">
    <div class="brand"><span class="brand-dot"></span>Silver Kettle</div>
    <div class="front-heading">
      <p class="tagline">Helping Build Businesses<br>One Step at a Time</p>
      <div class="rule"></div>
      <p class="person-name">Dana Whitfield, CPA</p>
      <p class="person-title">Director</p>
    </div>
  </div>
  <div class="front-band">
    <ul class="contact-list">
      <li><span class="contact-icon"><svg width="9" height="9" viewBox="0 0 10 10"><path d="M2 1l2 2-1 1.3c.6 1.2 1.5 2.1 2.7 2.7L7 6l2 2-1.2 1.5C4.4 9.2.8 5.6.5 2.2z" fill="#fff"/></svg></span>555-014-2290</li>
      <li><span class="contact-icon"><svg width="9" height="7" viewBox="0 0 10 8"><rect x=".5" y=".5" width="9" height="7" fill="none" stroke="#fff"/><path d="M.5.5L5 4.5 9.5.5" fill="none" stroke="#fff"/></svg></span>dana@silverkettle.com</li>
      <li><span class="contact-icon"><svg width="9" height="9" viewBox="0 0 10 10"><circle cx="5" cy="5" r="4.3" fill="none" stroke="#fff"/><path d="M.7 5h8.6M5 .7c-2 2.4-2 6.2 0 8.6M5 .7c2 2.4 2 6.2 0 8.6" fill="none" stroke="#fff" stroke-width=".8"/></svg></span>www.silverkettle.com</li>
    </ul>
    <address class="address" style="font-style:normal">
      <span class="company">Silver Kettle Co. Ltd.</span><br>
      1420 Alder Grove Avenue<br>
      Portland, Oregon, 97205
    </address>
  </div>
  <div class="front-stripe"></div>
</section>

<section class="card card--back" aria-label="Business card back">
  <div class="back-brand"><span class="brand-dot"></span>Silver Kettle</div>
  <div class="back-rule"></div>
  <p class="back-question">How can I help you build your business?</p>
  <ul class="services">
    <li>Strategic Plan &amp; Financial Forecasting</li>
    <li>Fundraising</li>
    <li>Small Business Oversight and HR</li>
  </ul>
</section>

</body>
</html>
```